Stationary Design for an engineering start-up.

Company name: Lumetra Plank Inc.

Our advanced materials company utilizes a patented process to spray-coat wood surfaces with metal. Metal is sprayed as a super-heated powder and fully conforms to the surface of the wood allowing for a wide range of applications. Metals used are COPPER and BRONZE.

We need a stationary package that includes Business Card, Letter Head, and Envelope.

- After we will submit a contest for a brochure design, so a winning designer will have advantage to take that project as well.

Target Market(s)

Our target market are building and industrial design professionals.

- Architects
- Designers
- Builders

Industry/Entity Type

Engineering

Requirements
Must have
• - All stationary must include our logo (attached)

Sizes:
Business card: Standard 3.5 by 2 inches. Landscape.

Letterhead: 8.5" x 11"

Envelopes:
One standard commercial size #10 (4 1/8" by 9 1/2")
One catalog size envelope (9" by 12")
Assume envelopes are one-sided (front print only)

- Use bleeds where applicable

- Include all fonts used.

File Format:
AI or PSD
** for letterhead please include MSWord template.
Nice to have
• Design style
- Take design style from our logo and attached images.
- Modern, sharp, minimalistic
- Sans fonts
- Don''t be afraid to use color background for business card.
We''re open to ideas of making the business card somehow representative of the product - metal coated wood.

```html
<!DOCTYPE html>
<html lang="en">
<head>
<meta charset="utf-8">
<title>Lumetra Plank Inc. — Business Card</title>
<link href="https://fonts.googleapis.com/css2?family=Questrial&display=swap" rel="stylesheet">
<style>
  :root {
    --bronze-dark: #3a2a16;
    --bronze-mid: #6b4f26;
    --bronze-light: #8f6d33;
    --gold-line: #c9a45a;
    --ink: #1e140b;
    --rust: #d8502a;
    --text-light: #fbf3e2;
  }
  html, body {
    margin: 0;
    padding: 0;
    width: 1000px;
    height: 1200px;
    overflow: hidden;
  }
  body {
    position: relative;
    font-family: "Questrial", "Century Gothic", sans-serif;
    background:
      radial-gradient(ellipse at 85% 15%, rgba(190,145,70,0.45), transparent 55%),
      radial-gradient(ellipse at 80% 90%, rgba(180,135,60,0.4), transparent 50%),
      linear-gradient(180deg, var(--bronze-mid) 0%, var(--bronze-dark) 35%, var(--bronze-mid) 55%, var(--bronze-dark) 70%, var(--bronze-light) 100%);
  }
  .card-frame {
    position: absolute;
    left: 69px;
    width: 863px;
    border: 1.5px solid var(--gold-line);
    box-sizing: border-box;
  }
  .card-front { top: 71px; height: 460px; }
  .card-back { top: 669px; height: 462px; }

  .brand-lockup {
    position: absolute;
    display: flex;
    flex-direction: column;
    align-items: center;
    color: var(--ink);
  }
  .brand-mark {
    background: var(--rust);
    border: 6px solid var(--ink);
    box-sizing: border-box;
  }
  .brand-name {
    color: var(--ink);
    letter-spacing: 0.08em;
    white-space: nowrap;
    line-height: 1;
  }
  .card-front .brand-lockup { left: 0; right: 0; top: 46px; }
  .card-front .brand-mark { width: 150px; height: 150px; }
  .card-front .brand-name { font-size: 62px; margin-top: 70px; }

  .card-back .brand-lockup { left: 0; width: 433px; top: 125px; }
  .card-back .brand-mark { width: 95px; height: 95px; border-width: 5px; }
  .card-back .brand-name { font-size: 32px; margin-top: 46px; letter-spacing: 0.06em; }

  .card-divider {
    position: absolute;
    left: 433px;
    top: 38px;
    width: 1.5px;
    height: 385px;
    background: var(--gold-line);
  }
  .contact {
    position: absolute;
    left: 466px;
    top: 36px;
    color: var(--text-light);
    text-shadow: 0 0 2px var(--ink), 0 1px 1px var(--ink);
  }
  .contact-name { font-size: 44px; margin: 0; line-height: 1.1; }
  .contact-role { font-size: 36px; margin: 0 0 28px; line-height: 1.1; }
  .contact-block { font-size: 25px; line-height: 29px; margin: 0 0 26px; font-style: normal; }
  .contact-web { font-size: 25px; margin: 0; }
</style>
</head>
<body>
  <section class="card-frame card-front" aria-label="Business card front">
    <div class="brand-lockup">
      <div class="brand-mark" aria-hidden="true"></div>
      <div class="brand-name">LUMETRA PLANK INC.</div>
    </div>
  </section>

  <section class="card-frame card-back" aria-label="Business card back">
    <div class="brand-lockup">
      <div class="brand-mark" aria-hidden="true"></div>
      <div class="brand-name">LUMETRA PLANK INC.</div>
    </div>
    <div class="card-divider"></div>
    <div class="contact">
      <p class="contact-name">Dalen R.</p>
      <p class="contact-role">Owner</p>
      <address class="contact-block">48 Harbour Rd.<br>Westvale<br>Province<br>4K7 2M9</address>
      <p class="contact-block">t. 555.018.2460<br>f. 555.018.2460</p>
      <p class="contact-web">www.lumetraplank.com</p>
    </div>
  </section>
</body>
</html>
```